Re-Design of Business Card for Marine Sales People

We are looking to Re-design our business cards to look like they are in the 21st century. We are a full service marina and sell a lot of new/used boats. May want a spot on the card for our 3 main brands we sell. A picture spot of the sales man would be nice, but not necessarily.

```html
<!DOCTYPE html>
<html lang="en">
<head>
<meta charset="utf-8">
<title>Harbor Pine Marine – Business Card</title>
<link rel="stylesheet" href="https://fonts.googleapis.com/css2?family=Poppins:wght@400;600;700&family=Lato:wght@400&family=Nunito:ital,wght@1,600&family=Libre+Baskerville:ital,wght@1,700&display=swap">
<style>
  :root {
    --backdrop: #e4dcd4;
    --card-white: #f4f4f4;
    --navy: #0d2a52;
    --navy-deep: #0a1f40;
    --accent-blue: #2a8fd0;
    --ink: #1f1f1f;
    --band-white: #ececec;
    --white: #ffffff;
  }
  * { box-sizing: border-box; margin: 0; padding: 0; }
  html, body { width: 1200px; height: 1057px; overflow: hidden; }
  body { background: var(--backdrop); position: relative; font-family: "Lato", sans-serif; }

  .card { position: absolute; left: 258px; width: 711px; height: 406px; overflow: hidden; }
  .card--front { top: 102px; background: var(--card-white); }
  .card--back { top: 549px; background: linear-gradient(135deg, var(--navy-deep), var(--navy)); }

  .front__band { position: absolute; left: 0; bottom: 0; width: 100%; height: 22px; background: var(--navy); }

  .brand { position: absolute; display: flex; align-items: center; gap: 12px; font-family: "Poppins", sans-serif; font-weight: 600; white-space: nowrap; }
  .brand__dot { border-radius: 50%; flex: none; background: var(--accent-blue); }
  .brand__name { line-height: 1; }

  .card--front .brand { left: 62px; top: 188px; color: var(--navy); }
  .card--front .brand__dot { width: 30px; height: 30px; }
  .card--front .brand__name { font-size: 24px; }

  .front__divider { position: absolute; left: 401px; top: 115px; width: 2px; height: 176px; background: var(--accent-blue); }

  .contact { position: absolute; left: 428px; top: 108px; color: var(--ink); }
  .contact__name { font-family: "Poppins", sans-serif; font-weight: 700; font-size: 24px; color: var(--navy); letter-spacing: .5px; line-height: 1.1; }
  .contact__tagline { font-family: "Poppins", sans-serif; font-size: 14px; margin-top: 1px; }
  .contact__address { font-size: 14.5px; line-height: 18px; margin-top: 14px; }
  .contact__list { list-style: none; margin-top: 7px; }
  .contact__list li { display: flex; align-items: center; gap: 6px; font-size: 14.5px; height: 21px; }
  .contact__list svg { width: 12px; height: 12px; fill: var(--accent-blue); flex: none; }

  .card--back .brand { left: 92px; top: 168px; color: var(--white); }
  .card--back .brand__dot { width: 36px; height: 36px; }
  .card--back .brand__name { font-size: 27px; }

  .slogan { position: absolute; left: 468px; top: 158px; width: 156px; text-align: center; color: var(--white); font-family: "Libre Baskerville", serif; font-style: italic; font-weight: 700; font-size: 16px; line-height: 27px; }
  .slogan__rule { display: block; height: 2px; width: 120px; margin: 0 auto; background: var(--accent-blue); }

  .locations { position: absolute; left: 90px; top: 219px; width: 532px; height: 29px; background: var(--band-white); border-radius: 3px 3px 12px 12px; display: flex; justify-content: space-between; align-items: center; padding: 0 6px; font-family: "Nunito", sans-serif; font-style: italic; font-weight: 600; font-size: 14.5px; color: var(--navy); }
</style>
</head>
<body>
  <section class="card card--front">
    <div class="brand">
      <span class="brand__dot"></span>
      <span class="brand__name">HARBOR PINE MARINE</span>
    </div>
    <div class="front__divider"></div>
    <div class="contact">
      <h1 class="contact__name">COLIN MERCER</h1>
      <p class="contact__tagline">Tagline Here</p>
      <p class="contact__address">48 Cove Road<br>Linden, NH 03110</p>
      <ul class="contact__list">
        <li><svg viewBox="0 0 12 12"><path d="M3 0h6a1 1 0 0 1 1 1v10a1 1 0 0 1-1 1H3a1 1 0 0 1-1-1V1a1 1 0 0 1 1-1zm0 1.5v8h6v-8z"/></svg>(603) 555-0142</li>
        <li><svg viewBox="0 0 12 12"><path d="M2.5 0.5l2 2.5-1 1.3c.7 1.5 1.8 2.6 3.2 3.2l1.3-1 2.5 2-1 2.2C5 10.5 1.5 7 .5 2z"/></svg>(603) 555-0142</li>
        <li><svg viewBox="0 0 12 12"><path d="M0 2h12v1L6 7 0 3zm0 2.3l6 4 6-4V10H0z"/></svg>info@harborpinemarine.com</li>
        <li><svg viewBox="0 0 12 12"><circle cx="6" cy="6" r="6"/></svg>www.harborpinemarine.com</li>
      </ul>
    </div>
    <div class="front__band"></div>
  </section>

  <section class="card card--back">
    <div class="brand">
      <span class="brand__dot"></span>
      <span class="brand__name">HARBOR PINE MARINE</span>
    </div>
    <p class="slogan">“Riding Tides”<span class="slogan__rule"></span>Since 1984</p>
    <div class="locations"><span>Cove Lake, Linden, NH</span><span>Pine Hollow Lake, Alder, NH</span></div>
  </section>
</body>
</html>
```